Design for mobile and web app for sweepstakes.

We need the design for a mobile app (planned to be build with jquery mobile) and web app (mobile first, we will use same look and feel as mobile just with displaying more info at once).

The following pages must be included:
- Userregistration/Login (Reg via Email, Chattrove-Reg)

- List of available sweepstakes (including some icons: a video icon, a "like button" type icon, a "provide some info" type of icon) this should be on the side in wep app but in mobile app its a list. possible is also a mobile display where users can swipe back and forth through it.

- single sweepstake detailview . should present a single sweepstake and give users the opportunity to participate with a button.

user settings. (doesnt not have to include a lot of fields we will at ourself. should contain some datepicker (birthday), some on/off switch (receive newsletters) some textfield in order for us to have a feel.

We have included the following files:
- glimmorica_logo_final01.png:
this is our logo which should be used and also the look and feel must fit with the logo.

- glimmorica_logo_final06.png:
this is the app-icon

-folie neu login registrierung :
this is a simple mockup for a registration page. the design doesnt have to contain all fields we will do that ourselfes starting from your handover, but should represent a common registration page with some fields

- funktionalität mit hässlichen buttons )
this is just a mockup for a possible design. not that it does use our old logo. This again is not binding is just to get a feel for what we are looking for. A list of sweepstakes and a detailspage for the sweepstake for users to participate in it.

Target Market(s)

German speaking users, Austria, Germany, Switzerland
The app is adressing a wide crowd of users who are interested in participating in sweepstakes.

Industry/Entity Type

Build

Number of Pages Required

4 page

Font styles to use
Sans Serif

Requirements
Must have
• - jquery and jquery mobile
• - html5 (preferable bootstrap-based)
• - css3
• - description on used fonts and colors. fonts must be free to use and publicly available for anyone to use.
• - all buttons should be css

```html
<!DOCTYPE html>
<html lang="de">
<head>
<meta charset="utf-8">
<title>glimmorica – Sweepstakes App Screens</title>
<link href="https://fonts.googleapis.com/css2?family=Source+Sans+3:ital,wght@0,400;0,600;0,700;1,400&display=swap" rel="stylesheet">
<style>
  :root{
    --navy:#172435;
    --green:#6fa132;
    --green-dark:#33502d;
    --yellow:#d8b42a;
    --yellow-light:#f2d46a;
    --paper:#edf1e7;
    --white:#ffffff;
    --text:#555a55;
    --muted:#a3a7a1;
    --icon:#c9ccc7;
  }
  *{box-sizing:border-box;margin:0;padding:0}
  html,body{width:1200px;height:1185px;overflow:hidden;background:var(--navy)}
  body{font-family:"Source Sans 3",sans-serif}
  svg{display:block}
  .board{position:absolute;left:0;top:0;width:1417px;height:1399px;transform:scale(.84686);transform-origin:0 0;background:var(--navy)}
  .screen{position:absolute;width:320px;overflow:hidden;background:var(--green)}
  .statusbar{position:absolute;left:0;top:0;width:100%;height:24px;background:var(--green);color:var(--white);font-family:Arial,sans-serif;font-size:12px}
  .statusbar > span{position:absolute;display:block;line-height:12px}
  .statusbar .dots{left:9px;top:8px;height:8px}
  .statusbar .carrier{left:55px;top:6px}
  .statusbar .wifi{left:92px;top:6px}
  .statusbar .time{left:141px;top:6px}
  .statusbar .pct{left:251px;top:6px}
  .statusbar .battery{left:283px;top:7px}
  .abs{position:absolute}
  .wordmark{position:absolute;width:100%;text-align:center;font-weight:700;letter-spacing:-1px}
  .mark-dot{display:inline-block;width:18px;height:18px;border-radius:50%;background:var(--yellow);margin-right:10px;vertical-align:middle;position:relative;top:-4px}
  .field{position:absolute;height:48px;border-radius:24px;background:var(--white);color:var(--text);font-size:16px;font-weight:600;line-height:48px;padding-left:50px;text-transform:uppercase}
  .field svg{position:absolute;left:23px;top:14px}
  .btn{position:absolute;height:48px;border-radius:24px;text-align:center;line-height:48px;font-size:16px;font-weight:700;color:var(--white);text-transform:uppercase;letter-spacing:.2px}
  .btn-yellow{background:var(--yellow)}
  .btn-outline{border:2px solid var(--white);line-height:44px}
  .topbar{position:absolute;left:0;top:24px;width:100%;height:58px;background:var(--paper);color:var(--text);font-size:20px;font-weight:600;text-align:center;line-height:56px}
  .topbar .left{position:absolute;left:16px;top:19px}
  .topbar .right{position:absolute;right:14px;top:19px}
  .photo{position:absolute;border-radius:50%;background:radial-gradient(circle at 60% 45%,#7fd0f0 0,#3a8fc4 25%,#d9b99c 45%,#6b4c3c 70%,#111 100%)}
  .row{position:absolute;left:0;width:320px;height:72px;background:var(--white);border-bottom:1px solid #e6e8e3}
  .row.active{background:var(--green)}
  .row .photo{left:7px;top:8px;width:54px;height:54px}
  .row .title{position:absolute;left:73px;top:5px;font-size:14px;color:var(--text)}
  .row .sub{position:absolute;left:73px;top:25px;font-size:13px;color:var(--yellow)}
  .row .date{position:absolute;left:73px;top:46px;font-size:11px;color:var(--muted)}
  .row.active .title,.row.active .sub,.row.active .date{color:var(--white)}
  .row .like{position:absolute;left:273px;top:19px;width:32px;height:32px;border-radius:50%;background:var(--yellow)}
  .row.active .like{background:var(--white)}
  .row .like svg{position:absolute;left:8px;top:8px}
</style>
</head>
<body>
<div class="board">

  <!-- Splash -->
  <section class="screen splash" style="left:160px;top:144px;height:480px;background:radial-gradient(circle at 50% 45%,#3c5a33,var(--green-dark))">
    <div class="statusbar" style="background:transparent">
      <span class="dots"><svg width="40" height="8"><g fill="#fff"><circle cx="4" cy="4" r="3.3"/><circle cx="12" cy="4" r="3.3"/><circle cx="20" cy="4" r="3.3"/></g><g fill="none" stroke="#fff"><circle cx="28" cy="4" r="3"/><circle cx="36" cy="4" r="3"/></g></svg></span>
      <span class="carrier">Ulva</span>
      <span class="wifi"><svg width="14" height="11" fill="none" stroke="#fff" stroke-width="1.6"><path d="M1 4a9 9 0 0 1 12 0M3.5 6.5a5 5 0 0 1 7 0"/><circle cx="7" cy="9" r="1" fill="#fff"/></svg></span>
      <span class="time">4:21PM</span><span class="pct">20%</span>
      <span class="battery"><svg width="28" height="11"><rect x=".5" y=".5" width="24" height="10" fill="none" stroke="#fff"/><rect x="2" y="2" width="5" height="7" fill="#fff"/><rect x="25" y="3" width="2" height="5" fill="#fff"/></svg></span>
    </div>
    <div class="wordmark" style="top:218px;font-size:48px;color:var(--white)"><span class="mark-dot"></span>glimmorica</div>
    <svg class="abs" style="left:115px;top:309px" width="90" height="90" viewBox="0 0 90 90">
      <circle cx="45" cy="45" r="38" fill="none" stroke="var(--yellow-light)" stroke-width="11" stroke-dasharray="20 4"/>
      <circle cx="45" cy="45" r="38" fill="none" stroke="var(--yellow)" stroke-width="11" stroke-dasharray="78.8 160" transform="rotate(90 45 45)"/>
      <text x="45" y="51" text-anchor="middle" fill="#fff" font-family="Source Sans 3, sans-serif" font-weight="700" font-size="18">33%</text>
    </svg>
  </section>

  <!-- Login -->
  <section class="screen login" style="left:543px;top:144px;height:536px">
    <div class="statusbar">
      <span class="dots"><svg width="40" height="8"><g fill="#fff"><circle cx="4" cy="4" r="3.3"/><circle cx="12" cy="4" r="3.3"/><circle cx="20" cy="4" r="3.3"/></g><g fill="none" stroke="#fff"><circle cx="28" cy="4" r="3"/><circle cx="36" cy="4" r="3"/></g></svg></span>
      <span class="carrier">Ulva</span>
      <span class="wifi"><svg width="14" height="11" fill="none" stroke="#fff" stroke-width="1.6"><path d="M1 4a9 9 0 0 1 12 0M3.5 6.5a5 5 0 0 1 7 0"/><circle cx="7" cy="9" r="1" fill="#fff"/></svg></span>
      <span class="time">4:21PM</span><span class="pct">20%</span>
      <span class="battery"><svg width="28" height="11"><rect x=".5" y=".5" width="24" height="10" fill="none" stroke="#fff"/><rect x="2" y="2" width="5" height="7" fill="#fff"/><rect x="25" y="3" width="2" height="5" fill="#fff"/></svg></span>
    </div>
    <div class="abs" style="left:0;top:24px;width:320px;height:170px;background:var(--paper);border-bottom:6px solid #5d8a2b"></div>
    <div class="wordmark" style="top:132px;font-size:44px;color:var(--green)"><span class="mark-dot"></span>glimmorica</div>
    <div class="field" style="left:34px;top:223px;width:253px"><svg width="20" height="20" viewBox="0 0 20 20" fill="var(--icon)"><circle cx="10" cy="6" r="5"/><path d="M0 20c0-6 4-8 10-8s10 2 10 8z"/></svg>Email Address</div>
    <div class="field" style="left:34px;top:283px;width:253px"><svg width="16" height="20" viewBox="0 0 16 20" fill="var(--icon)"><path d="M3 9V6a5 5 0 0 1 10 0v3h-2V6a3 3 0 0 0-6 0v3z"/><rect y="9" width="16" height="11" rx="1"/></svg>Password</div>
    <div class="btn btn-yellow" style="left:34px;top:343px;width:253px">Login</div>
    <div class="abs" style="left:75px;top:415px;color:#fff;font-size:16px;font-weight:700;line-height:20px;padding-left:28px">
      <svg class="abs" style="left:0;top:0" width="20" height="20"><circle cx="10" cy="10" r="10" fill="#fff"/><text x="10" y="15" text-anchor="middle" fill="var(--green)" font-family="Source Sans 3,sans-serif" font-weight="700" font-size="14">?</text></svg>FORGOT PASSWORD</div>
    <div class="btn btn-outline" style="left:34px;top:461px;width:253px">New Registeration</div>
  </section>

  <!-- Registration -->
  <section class="screen register" style="left:921px;top:144px;height:757px">
    <div class="statusbar">
      <span class="dots"><svg width="40" height="8"><g fill="#fff"><circle cx="4" cy="4" r="3.3"/><circle cx="12" cy="4" r="3.3"/><circle cx="20" cy="4" r="3.3"/></g><g fill="none" stroke="#fff"><circle cx="28" cy="4" r="3"/><circle cx="36" cy="4" r="3"/></g></svg></span>
      <span class="carrier">Ulva</span>
      <span class="wifi"><svg width="14" height="11" fill="none" stroke="#fff" stroke-width="1.6"><path d="M1 4a9 9 0 0 1 12 0M3.5 6.5a5 5 0 0 1 7 0"/><circle cx="7" cy="9" r="1" fill="#fff"/></svg></span>
      <span class="time">4:21PM</span><span class="pct">20%</span>
      <span class="battery"><svg width="28" height="11"><rect x=".5" y=".5" width="24" height="10" fill="none" stroke="#fff"/><rect x="2" y="2" width="5" height="7" fill="#fff"/><rect x="25" y="3" width="2" height="5" fill="#fff"/></svg></span>
    </div>
    <div class="topbar">New Registration
      <svg class="left" width="18" height="16"><g stroke="var(--yellow)" stroke-width="2"><path d="M0 2h18M0 8h18M0 14h18"/></g></svg>
      <svg class="right" width="16" height="16" viewBox="0 0 16 16"><circle cx="8" cy="8" r="5.5" fill="none" stroke="var(--yellow)" stroke-width="4" stroke-dasharray="2.6 1.7"/><circle cx="8" cy="8" r="4.5" fill="var(--yellow)"/><circle cx="8" cy="8" r="2" fill="var(--paper)"/></svg>
    </div>
    <div class="field" style="left:33px;top:114px;width:253px"><svg width="20" height="20" viewBox="0 0 20 20" fill="var(--icon)"><circle cx="10" cy="6" r="5"/><path d="M0 20c0-6 4-8 10-8s10 2 10 8z"/></svg>Email Address</div>
    <div class="field" style="left:33px;top:174px;width:253px"><svg width="16" height="20" viewBox="0 0 16 20" fill="var(--icon)"><path d="M3 9V6a5 5 0 0 1 10 0v3h-2V6a3 3 0 0 0-6 0v3z"/><rect y="9" width="16" height="11" rx="1"/></svg>Password</div>
    <div class="field" style="left:33px;top:235px;width:253px"><svg width="16" height="20" viewBox="0 0 16 20" fill="var(--icon)"><path d="M3 9V6a5 5 0 0 1 10 0v3h-2V6a3 3 0 0 0-6 0v3z"/><rect y="9" width="16" height="11" rx="1"/></svg>Retype Password</div>
    <div class="field" style="left:33px;top:295px;width:153px;padding-left:21px">India
      <svg style="left:115px;top:10px" width="28" height="28"><circle cx="14" cy="14" r="14" fill="var(--yellow)"/><path d="M9 12l5 5 5-5" fill="none" stroke="#fff" stroke-width="2.4"/></svg></div>
    <div class="field" style="left:197px;top:295px;width:89px;padding-left:20px">PLZ</div>
    <div class="field" style="left:33px;top:356px;width:253px"><svg width="17" height="17" viewBox="0 0 17 17" fill="none" stroke="var(--icon)" stroke-width="1.5"><rect x="1" y="3" width="15" height="13"/><path d="M1 7h15M5 1v4M12 1v4"/></svg>Geb. Datum</div>
    <div class="abs" style="left:33px;top:414px;width:250px;color:#fff;font-size:15px;font-weight:700;line-height:20px;padding-left:29px">
      <svg class="abs" style="left:0;top:2px" width="20" height="20"><circle cx="10" cy="10" r="10" fill="#fff"/><rect x="9" y="8" width="2.4" height="7.5" fill="var(--green)"/><circle cx="10.2" cy="5.5" r="1.4" fill="var(--green)"/></svg>
      Mobile-Nummer zrur sms autheentifizierung</div>
    <div class="field" style="left:33px;top:463px;width:253px;font-size:15px;text-transform:none"><svg width="16" height="16" viewBox="0 0 16 16"><path d="M3 1l3 3-2 2c1 2 4 5 6 6l2-2 3 3-2 2C8 15 1 8 1 3z" fill="var(--icon)"/></svg>+91-987654XXXX</div>
    <div class="btn btn-yellow" style="left:33px;top:525px;width:166px">Code Anfordern</div>
    <div class="field" style="left:211px;top:525px;width:75px;padding-left:15px;font-size:15px">98765</div>
    <div class="abs" style="left:34px;top:582px;color:#fff;font-size:15px;font-weight:700">4 Stelliger autheentifizierung Code</div>
    <div class="btn btn-outline" style="left:33px;top:623px;width:253px">Registrieren</div>
    <p class="abs" style="left:33px;top:681px;width:260px;color:#fff;font-size:13px;font-style:italic;line-height:20px">Lorem ipsum dolor sit amet, consectetur adipiscing elit. <span style="color:var(--yellow-light)">Aenean pharetra quis</span> odio sit amet porttitor. Cum sociis natoque</p>
  </section>

  <!-- Sweepstakes list -->
  <section class="screen list" style="left:160px;top:680px;height:513px;background:var(--white)">
    <div class="statusbar">
      <span class="dots"><svg width="40" height="8"><g fill="#fff"><circle cx="4" cy="4" r="3.3"/><circle cx="12" cy="4" r="3.3"/><circle cx="20" cy="4" r="3.3"/></g><g fill="none" stroke="#fff"><circle cx="28" cy="4" r="3"/><circle cx="36" cy="4" r="3"/></g></svg></span>
      <span class="carrier">Ulva</span>
      <span class="wifi"><svg width="14" height="11" fill="none" stroke="#fff" stroke-width="1.6"><path d="M1 4a9 9 0 0 1 12 0M3.5 6.5a5 5 0 0 1 7 0"/><circle cx="7" cy="9" r="1" fill="#fff"/></svg></span>
      <span class="time">4:21PM</span><span class="pct">20%</span>
      <span class="battery"><svg width="28" height="11"><rect x=".5" y=".5" width="24" height="10" fill="none" stroke="#fff"/><rect x="2" y="2" width="5" height="7" fill="#fff"/><rect x="25" y="3" width="2" height="5" fill="#fff"/></svg></span>
    </div>
    <div class="topbar">Available Sweepstakes
      <svg class="left" width="18" height="16"><g stroke="var(--yellow)" stroke-width="2"><path d="M0 2h18M0 8h18M0 14h18"/></g></svg>
      <svg class="right" width="16" height="16" viewBox="0 0 16 16"><circle cx="8" cy="8" r="5.5" fill="none" stroke="var(--yellow)" stroke-width="4" stroke-dasharray="2.6 1.7"/><circle cx="8" cy="8" r="4.5" fill="var(--yellow)"/><circle cx="8" cy="8" r="2" fill="var(--paper)"/></svg>
    </div>
    <div class="row" style="top:82px"><div class="photo" role="img" aria-label="Photo of a smartphone held in a hand"></div><span class="title">Lumo 5S</span><span class="sub">Therme XY</span><span class="date">bis 15.12.2014</span><span class="like"><svg width="16" height="16" viewBox="0 0 16 16" fill="#fff"><rect x="1" y="7" width="3" height="8"/><path d="M5 7l3-6c1.5 0 2 1 1.6 2.5L9 6h5.5a1.3 1.3 0 0 1 0 2.6 1.3 1.3 0 0 1 0 2.4 1.3 1.3 0 0 1-.3 2.4 1.2 1.2 0 0 1-1 1.6H5z"/></svg></span></div>
    <div class="row" style="top:154px"><div class="photo" role="img" aria-label="Photo of a smartphone held in a hand"></div><span class="title">Lumo 5S</span><span class="sub">Therme XY</span><span class="date">bis 15.12.2014</span><span class="like"><svg width="16" height="16" viewBox="0 0 16 16" fill="#fff"><rect x="1" y="7" width="3" height="8"/><path d="M5 7l3-6c1.5 0 2 1 1.6 2.5L9 6h5.5a1.3 1.3 0 0 1 0 2.6 1.3 1.3 0 0 1 0 2.4 1.3 1.3 0 0 1-.3 2.4 1.2 1.2 0 0 1-1 1.6H5z"/></svg></span></div>
    <div class="row active" style="top:226px"><div class="photo" role="img" aria-label="Photo of a smartphone held in a hand"></div><span class="title">Lumo 5S</span><span class="sub">Therme XY</span><span class="date">bis 15.12.2014</span><span class="like"><svg width="16" height="16" viewBox="0 0 16 16" fill="var(--green)"><rect x="1" y="7" width="3" height="8"/><path d="M5 7l3-6c1.5 0 2 1 1.6 2.5L9 6h5.5a1.3 1.3 0 0 1 0 2.6 1.3 1.3 0 0 1 0 2.4 1.3 1.3 0 0 1-.3 2.4 1.2 1.2 0 0 1-1 1.6H5z"/></svg></span></div>
    <div class="row" style="top:298px"><div class="photo" role="img" aria-label="Photo of a smartphone held in a hand"></div><span class="title">Lumo 5S</span><span class="sub">Therme XY</span><span class="date">bis 15.12.2014</span><span class="like"><svg width="16" height="16" viewBox="0 0 16 16" fill="#fff"><rect x="1" y="7" width="3" height="8"/><path d="M5 7l3-6c1.5 0 2 1 1.6 2.5L9 6h5.5a1.3 1.3 0 0 1 0 2.6 1.3 1.3 0 0 1 0 2.4 1.3 1.3 0 0 1-.3 2.4 1.2 1.2 0 0 1-1 1.6H5z"/></svg></span></div>
    <div class="row" style="top:370px"><div class="photo" role="img" aria-label="Photo of a smartphone held in a hand"></div><span class="title">Lumo 5S</span><span class="sub">Therme XY</span><span class="date">bis 15.12.2014</span><span class="like"><svg width="16" height="16" viewBox="0 0 16 16" fill="#fff"><rect x="1" y="7" width="3" height="8"/><path d="M5 7l3-6c1.5 0 2 1 1.6 2.5L9 6h5.5a1.3 1.3 0 0 1 0 2.6 1.3 1.3 0 0 1 0 2.4 1.3 1.3 0 0 1-.3 2.4 1.2 1.2 0 0 1-1 1.6H5z"/></svg></span></div>
    <div class="row" style="top:442px;border-bottom:0"><div class="photo" role="img" aria-label="Photo of a smartphone held in a hand"></div><span class="title">Lumo 5S</span><span class="sub">Therme XY</span><span class="date">bis 15.12.2014</span><span class="like"><svg width="16" height="16" viewBox="0 0 16 16" fill="#fff"><rect x="1" y="7" width="3" height="8"/><path d="M5 7l3-6c1.5 0 2 1 1.6 2.5L9 6h5.5a1.3 1.3 0 0 1 0 2.6 1.3 1.3 0 0 1 0 2.4 1.3 1.3 0 0 1-.3 2.4 1.2 1.2 0 0 1-1 1.6H5z"/></svg></span></div>
    <svg class="abs" style="left:207px;top:281px" width="16" height="20" viewBox="0 0 16 20"><path d="M5 1.5a1.3 1.3 0 0 1 2.6 0V9l1-.2V7a1.2 1.2 0 0 1 2.4 0v2l1-.1a1.2 1.2 0 0 1 2.3.4V14c0 3-2 5-5 5H8c-2 0-3-1-4-2.5L1.5 12a1.2 1.2 0 0 1 2-1.3L5 12z" fill="#fff" stroke="#222" stroke-width="1"/></svg>
  </section>

  <!-- Detail -->
  <section class="screen detail" style="left:543px;top:740px;height:524px;background:var(--white)">
    <div class="statusbar">
      <span class="dots"><svg width="40" height="8"><g fill="#fff"><circle cx="4" cy="4" r="3.3"/><circle cx="12" cy="4" r="3.3"/><circle cx="20" cy="4" r="3.3"/></g><g fill="none" stroke="#fff"><circle cx="28" cy="4" r="3"/><circle cx="36" cy="4" r="3"/></g></svg></span>
      <span class="carrier">Ulva</span>
      <span class="wifi"><svg width="14" height="11" fill="none" stroke="#fff" stroke-width="1.6"><path d="M1 4a9 9 0 0 1 12 0M3.5 6.5a5 5 0 0 1 7 0"/><circle cx="7" cy="9" r="1" fill="#fff"/></svg></span>
      <span class="time">4:21PM</span><span class="pct">20%</span>
      <span class="battery"><svg width="28" height="11"><rect x=".5" y=".5" width="24" height="10" fill="none" stroke="#fff"/><rect x="2" y="2" width="5" height="7" fill="#fff"/><rect x="25" y="3" width="2" height="5" fill="#fff"/></svg></span>
    </div>
    <div class="topbar" style="height:134px">Lumo Phone 4S
      <svg class="left" width="18" height="18" style="top:20px"><circle cx="9" cy="9" r="9" fill="var(--yellow)"/><path d="M10.5 5L7 9l3.5 4" fill="none" stroke="#fff" stroke-width="2"/></svg>
      <svg class="right" width="16" height="16" viewBox="0 0 16 16"><circle cx="8" cy="8" r="5.5" fill="none" stroke="var(--yellow)" stroke-width="4" stroke-dasharray="2.6 1.7"/><circle cx="8" cy="8" r="4.5" fill="var(--yellow)"/><circle cx="8" cy="8" r="2" fill="var(--paper)"/></svg>
    </div>
    <div class="photo" style="left:86px;top:82px;width:148px;height:148px" role="img" aria-label="Photo of a smartphone held in a hand"></div>
    <svg class="abs" style="left:190px;top:199px" width="31" height="31"><circle cx="15.5" cy="15.5" r="15.5" fill="var(--yellow)"/><circle cx="13.5" cy="13.5" r="4.5" fill="none" stroke="#fff" stroke-width="2.2"/><path d="M17 17l5 5" stroke="#fff" stroke-width="2.6"/></svg>
    <div class="abs" style="left:15px;top:259px;width:52px;height:52px;border-radius:50%;background:var(--paper)"></div>
    <div class="abs" style="left:80px;top:261px;color:var(--green);font-size:17px;font-weight:700">Therme XY</div>
    <div class="abs" style="left:82px;top:285px;color:var(--muted);font-size:11px">bis 15.12.2014</div>
    <p class="abs" style="left:15px;top:318px;width:295px;color:var(--text);font-size:13px;line-height:20px">Vivamus egestas porttitor diam eget dictum. Cras vel gravida metus. Curabitur velit turpis, phare-tra sed Vivamus lorem massa, vehicula a pretium ac, bibendum et mauris. Suspendisse sagittis mollis tortor, nec faucibus purus elementum a Integer ligula mi, luctus ac volutpat mollis.</p>
    <div class="btn btn-yellow" style="left:16px;top:454px;width:288px">Ein Klick zur Teilnahme</div>
  </section>

</div>
</body>
</html>
```